Blog based website for baseball.

I am a college baseball coach looking to create a blog type site that uses content to keep readers coming back and eventually trusting me enough to buy my products.

I am an author, coach, writer, speaker with a bunch sites now, but I want to make one main site that people can come back to and see new content over and over..

Target Market(s)

High school baseball players and parents.

Industry/Entity Type

Education

Number of Pages Required

4 page

Font styles to use
Sans Serif

Requirements
Must have
• 1) An about page. 2) Either commerce page or link to my other commerce pages. 3) Featured blog but also access to past blogs. 4) Featured product of the week (maybe in side bar). 5) Places to opt in and join the list. 6) A way to share the content people like.
Nice to have
• No idea the difference between uncoded and coded!
• I like the idea of an opt in pop up.

```html
<!DOCTYPE html>
<html lang="en">
<head>
<meta charset="utf-8">
<title>Diamond Coach</title>
<link href="https://fonts.googleapis.com/css2?family=Arimo:wght@400;700&family=Tinos:wght@400;700&display=swap" rel="stylesheet">
<style>
:root{
  --red:#e0201c;
  --ink:#333333;
  --grey:#6f6f6f;
  --light:#9a9a9a;
  --blue:#1f3fd0;
  --dark:#3b3b3b;
  --darker:#2e2e2e;
  --rule:#d8d8d8;
  --white:#ffffff;
}
*{margin:0;padding:0;box-sizing:border-box}
html,body{width:1200px;height:2728px;overflow:hidden;background:var(--white)}
body{position:relative;font-family:"Arimo",Arial,sans-serif;color:var(--grey)}
.serif{font-family:"Tinos","Times New Roman",serif}
.abs{position:absolute}

/* header */
.brand{left:72px;top:62px;display:flex;align-items:center;gap:14px}
.brand-dot{width:34px;height:34px;border-radius:50%;background:var(--red)}
.brand-name{font-family:"Arimo",Arial,sans-serif;font-weight:700;font-size:34px;color:var(--red);letter-spacing:1px}
.nav{left:478px;top:100px;display:flex;gap:0;list-style:none}
.nav li{font-size:15px;font-weight:700;color:var(--red);padding:14px 26px;text-transform:uppercase;letter-spacing:.5px}
.nav li.active{background:var(--red);color:var(--white)}

/* hero */
.hero-title{left:80px;top:318px;width:640px;font-size:90px;line-height:94px;color:var(--red);font-weight:400}
.hero-photo{left:690px;top:168px;width:470px;height:620px;background:linear-gradient(180deg,#f4f4f4 0%,#cfcfcf 45%,#2b2b2b 100%)}
.hero-dots{left:106px;top:770px;display:flex;gap:10px}
.hero-dots span{width:12px;height:12px;border-radius:50%;background:var(--blue)}
.hero-dots span.on{background:var(--red)}

/* about */
.about-title{left:0;top:812px;width:1200px;text-align:center;font-size:62px;color:var(--grey)}
.about-text{left:96px;top:900px;width:1008px;text-align:center;font-size:15px;line-height:22px;color:var(--light)}
.read-more{font-size:14px;color:var(--red);text-transform:uppercase;letter-spacing:.5px}
.about-more{left:0;top:1062px;width:1200px;text-align:center}
.rule{left:80px;top:1100px;width:1040px;height:2px;background:var(--rule)}

/* feature */
.feature-title{left:80px;top:1124px;width:520px;font-size:60px;line-height:62px;color:var(--grey)}
.feature-lead{left:80px;top:1334px;width:520px;font-size:25px;line-height:30px;color:var(--blue);text-transform:uppercase}
.feature-img{top:1132px;width:254px;height:268px}
.fi-1{left:620px;background:linear-gradient(180deg,#d9e4ea 0%,#9aa89a 60%,#8a6d4a 100%)}
.fi-2{left:888px;background:linear-gradient(180deg,#f2f4fb 0%,#dfe4f6 100%)}
.feature-cap{top:1420px;width:250px;font-size:14px;line-height:20px;color:var(--light)}
.fc-1{left:620px}.fc-2{left:888px}
.slider-arrows{left:1104px;top:1562px;display:flex;gap:6px}

/* products */
.products-title{left:80px;top:1614px;font-size:58px;color:var(--grey)}
.product{left:80px;width:520px;display:flex;gap:40px}
.product svg{flex:none}
.product h3{font-size:21px;font-weight:400;color:var(--ink);text-transform:uppercase;margin-top:4px}
.product p{font-size:14px;line-height:19px;color:var(--grey);width:360px;margin-top:4px}
.p-1{top:1714px}.p-2{top:1826px}.p-3{top:1946px}
.product-img{width:222px;height:180px;background:linear-gradient(180deg,#6f8a52 0%,#a3825c 70%,#c29f72 100%);border:4px solid #e9e9e9}
.pi-1{left:652px;top:1632px}.pi-2{left:912px;top:1632px}
.pi-3{left:652px;top:1840px}.pi-4{left:912px;top:1840px}

/* dark band */
.band{left:0;top:2064px;width:1200px;height:382px;background:var(--dark)}
.band-title{top:2070px;font-size:60px;color:var(--white)}
.bt-blog{left:80px}.bt-arch{left:740px}
.post{left:88px;width:630px;display:flex;gap:24px;align-items:flex-start}
.post p{font-size:13px;line-height:19px;color:#cfcfcf;width:560px}
.post-1{top:2172px}.post-2{top:2252px}.post-3{top:2332px}
.archive{left:760px;top:2168px;list-style:none}
.archive li{font-size:13px;line-height:30px;color:#cfcfcf;display:flex;align-items:center;gap:18px}
.band-link{top:2412px;font-size:13px;color:var(--white);text-transform:uppercase;letter-spacing:.5px}
.bl-blog{left:340px}.bl-arch{left:866px}

/* map */
.map{left:0;top:2446px;width:1200px;height:282px;background:linear-gradient(135deg,#e8e6df 0%,#dcdcd2 50%,#e6e2d6 100%)}
.foot-brand{left:884px;top:2620px;display:flex;align-items:center;gap:12px}
</style>
</head>
<body>

<header>
  <div class="abs brand"><span class="brand-dot"></span><span class="brand-name">DIAMOND COACH</span></div>
  <ul class="abs nav">
    <li class="active">Home</li><li>Portfolios</li><li>Blog</li><li>About Us</li><li>Contacts</li>
  </ul>
</header>

<section class="hero">
  <h1 class="abs hero-title serif">LOREM IPSUM DOLOR SIT AMET</h1>
  <div class="abs hero-photo" role="img" aria-label="Photo of the coach in a black shirt holding a clipboard"></div>
  <div class="abs hero-dots"><span class="on"></span><span></span><span></span></div>
</section>

<section class="about">
  <h2 class="abs about-title serif">ABOUT ME</h2>
  <p class="abs about-text">Lorem ipsum dolor sit amet, consectetur adipiscing elit. Aenean commodo ligula eget dolor. Aenean massa. Cum sociis natoque penatibus et magnis dis parturient montes, nascetur ridiculus mus. Donec quam felis, ultricies nec, pellentesque eu, pretium quis, sem. Nulla consequat massa quis enim. Donec pede justo, fringilla vel, aliquet nec, vulputate eget, arcu. In enim justo, rhoncus ut, imperdiet a, venenatis vitae, justo. Nullam dictum felis eu pede mollis pretium. Cras dapibus.</p>
  <div class="abs about-more read-more serif">Read More &#9656;</div>
  <div class="abs rule"></div>
</section>

<section class="feature">
  <h2 class="abs feature-title serif">LOREM IPSUM DOLOR SIT DOL OR SIT</h2>
  <p class="abs feature-lead serif">Lorem ipsum dolor sit amet, consectetuer adipiscing elit. Aenean commodo ligula eget dolor. Aenean massa. Cum sociis natoque penatibus et</p>
  <div class="abs feature-img fi-1" role="img" aria-label="Photo of a baseball on a dirt infield"></div>
  <div class="abs feature-img fi-2" role="img" aria-label="Illustration of a batter silhouette in blue"></div>
  <p class="abs feature-cap fc-1">Lorem ipsum dolor sit amet, consectetur adipiscing elit. Aenean commodo ligula eget dolor. Cum sociis natoque penatibus et.</p>
  <p class="abs feature-cap fc-2">Lorem ipsum dolor sit amet, consectetur adipiscing elit. Aenean commodo ligula eget dolor. Cum sociis natoque penatibus et.</p>
  <div class="abs slider-arrows">
    <svg width="14" height="16" viewBox="0 0 14 16"><path d="M12 1 L2 8 L12 15Z" fill="#8a8a8a"/></svg>
    <svg width="14" height="16" viewBox="0 0 14 16"><path d="M2 1 L12 8 L2 15Z" fill="#8a8a8a"/></svg>
  </div>
</section>

<section class="products">
  <h2 class="abs products-title serif">NEW PRODUCTS</h2>
  <div class="abs product p-1">
    <svg width="84" height="80" viewBox="0 0 84 80"><g fill="#222"><rect x="2" y="8" width="12" height="70"/><rect x="18" y="2" width="12" height="76"/><rect x="34" y="12" width="12" height="66"/><rect x="52" y="10" width="12" height="68" transform="rotate(-14 58 44)"/><rect x="0" y="76" width="84" height="4"/></g></svg>
    <div><h3>Education Program</h3><p>Lorem ipsum dolor sit amet, ultricies nec, pellentesque eu, pretium quis, sem. Nulla consequat massa.</p></div>
  </div>
  <div class="abs product p-2">
    <svg width="84" height="80" viewBox="0 0 84 80"><rect x="4" y="2" width="76" height="52" fill="#222"/><rect x="10" y="8" width="64" height="40" fill="#fff"/><rect x="34" y="54" width="16" height="12" fill="#222"/><rect x="22" y="66" width="40" height="6" fill="#222"/></svg>
    <div><h3>Market Research</h3><p>Lorem ipsum dolor sit amet, ultricies nec, pellentesque eu, pretium quis, sem. Nulla consequat massa.</p></div>
  </div>
  <div class="abs product p-3">
    <svg width="84" height="80" viewBox="0 0 84 80"><g fill="#222"><circle cx="16" cy="14" r="9"/><rect x="8" y="26" width="16" height="30"/><rect x="8" y="56" width="6" height="22"/><rect x="18" y="56" width="6" height="22"/><rect x="34" y="4" width="48" height="4"/><rect x="36" y="8" width="44" height="34" fill="none" stroke="#222" stroke-width="3"/><rect x="56" y="42" width="4" height="36"/><rect x="22" y="30" width="18" height="4" transform="rotate(-30 22 32)"/></g></svg>
    <div><h3>Training Program</h3><p>Lorem ipsum dolor sit amet, ultricies nec, pellentesque eu, pretium quis, sem. Nulla consequat massa.</p></div>
  </div>
  <div class="abs product-img pi-1" role="img" aria-label="Photo of a batter at the plate"></div>
  <div class="abs product-img pi-2" role="img" aria-label="Photo of a batter following through"></div>
  <div class="abs product-img pi-3" role="img" aria-label="Photo of a batter waiting for the pitch"></div>
  <div class="abs product-img pi-4" role="img" aria-label="Photo of a batter mid swing"></div>
</section>

<section class="blog">
  <div class="abs band"></div>
  <h2 class="abs band-title bt-blog serif">FEATURED BLOG</h2>
  <h2 class="abs band-title bt-arch serif">ARCHIVE</h2>
  <div class="abs post post-1">
    <svg width="22" height="22" viewBox="0 0 22 22"><path d="M4 2 L18 11 L4 20Z" fill="#9a9a9a"/></svg>
    <p>Lorem ipsum dolor sit amet, consectetur adipiscing elit. Aenean commodo ligula eget dolor. Aenean massa. Cum sociis natoque penatibus et magnis dis parturient montes, nascetur ridiculus mus. Donec quam felis.</p>
  </div>
  <div class="abs post post-2">
    <svg width="22" height="22" viewBox="0 0 22 22"><path d="M4 2 L18 11 L4 20Z" fill="#9a9a9a"/></svg>
    <p>Lorem ipsum dolor sit amet, consectetur adipiscing elit. Aenean commodo ligula eget dolor. Aenean massa. Cum sociis natoque penatibus et magnis dis parturient montes, nascetur ridiculus mus. Donec quam felis.</p>
  </div>
  <div class="abs post post-3">
    <svg width="22" height="22" viewBox="0 0 22 22"><path d="M4 2 L18 11 L4 20Z" fill="#9a9a9a"/></svg>
    <p>Lorem ipsum dolor sit amet, consectetur adipiscing elit. Aenean commodo ligula eget dolor. Aenean massa. Cum sociis natoque penatibus et magnis dis parturient montes, nascetur ridiculus mus. Donec quam felis.</p>
  </div>
  <ul class="abs archive">
    <li><svg width="12" height="12" viewBox="0 0 12 12"><path d="M2 1 L10 6 L2 11Z" fill="#9a9a9a"/></svg>Lorem ipsum dolor sit amet 2014 (12)</li>
    <li><svg width="12" height="12" viewBox="0 0 12 12"><path d="M2 1 L10 6 L2 11Z" fill="#9a9a9a"/></svg>Lorem ipsum dolor sit amet 2014 (10)</li>
    <li><svg width="12" height="12" viewBox="0 0 12 12"><path d="M2 1 L10 6 L2 11Z" fill="#9a9a9a"/></svg>Lorem ipsum dolor sit amet 2013 (18)</li>
    <li><svg width="12" height="12" viewBox="0 0 12 12"><path d="M2 1 L10 6 L2 11Z" fill="#9a9a9a"/></svg>Lorem ipsum dolor sit amet 2013 (14)</li>
    <li><svg width="12" height="12" viewBox="0 0 12 12"><path d="M2 1 L10 6 L2 11Z" fill="#9a9a9a"/></svg>Lorem ipsum dolor sit amet 2013 (16)</li>
    <li><svg width="12" height="12" viewBox="0 0 12 12"><path d="M2 1 L10 6 L2 11Z" fill="#9a9a9a"/></svg>Lorem ipsum dolor sit amet 2012 (09)</li>
    <li><svg width="12" height="12" viewBox="0 0 12 12"><path d="M2 1 L10 6 L2 11Z" fill="#9a9a9a"/></svg>Lorem ipsum dolor sit amet 2012 (11)</li>
    <li><svg width="12" height="12" viewBox="0 0 12 12"><path d="M2 1 L10 6 L2 11Z" fill="#9a9a9a"/></svg>Lorem ipsum dolor sit amet 2012 (07)</li>
  </ul>
  <div class="abs band-link bl-blog serif">Read More Blog Post</div>
  <div class="abs band-link bl-arch serif">More Archive</div>
</section>

<footer>
  <div class="abs map" role="img" aria-label="Street map showing the location"></div>
  <div class="abs foot-brand"><span class="brand-dot"></span><span class="brand-name">DIAMOND COACH</span></div>
</footer>

</body>
</html>
```